Ferndale Chapel of Grace (this will be used for new church sign) sign will be 4'x8' and would like also listed Sunday School 9:00am Worship Service 10:30am.

Logo Text

FERNDALE CHAPEL OF GRACE

```html
<!DOCTYPE html>
<html lang="en">
<head>
<meta charset="utf-8">
<title>Ferndale Chapel of Grace – Sign</title>
<link href="https://fonts.googleapis.com/css2?family=Cinzel:wght@600;700&family=Kalam:wght@700&display=swap" rel="stylesheet">
<style>
  :root {
    --backdrop: #e6e6e6;
    --night: #0a0b0d;
    --paper: #ffffff;
    --ink: #111111;
    --gold-deep: #c18f2c;
    --gold-bright: #f9c826;
    --gold-pale: #faf3c2;
    --gold-mid: #e2be6a;
    --gold-title-top: #fff0a8;
    --gold-title-bottom: #c8901e;
  }
  * { margin: 0; padding: 0; box-sizing: border-box; }
  html, body {
    width: 1200px;
    height: 1096px;
    overflow: hidden;
    background: var(--backdrop);
  }
  .sign {
    position: absolute;
    left: 50px;
    top: 273px;
    width: 1100px;
    height: 550px;
    overflow: hidden;
  }
  .sign-field {
    position: absolute;
    inset: 0;
    width: 100%;
    height: 100%;
  }
  .sign-name {
    position: absolute;
    left: 0;
    width: 100%;
    text-align: center;
  }
  .sign-name__place {
    top: 70px;
    font-family: "Kalam", cursive;
    font-weight: 700;
    font-size: 82px;
    line-height: 1;
    color: var(--paper);
  }
  .sign-name__church {
    top: 168px;
    font-family: "Cinzel", serif;
    font-weight: 700;
    font-size: 76px;
    line-height: 1;
    letter-spacing: 1px;
    background: linear-gradient(180deg, var(--gold-title-top) 0%, #f1c94a 45%, var(--gold-title-bottom) 100%);
    -webkit-background-clip: text;
    background-clip: text;
    color: transparent;
  }
  .cross {
    position: absolute;
    left: 521px;
    top: 303px;
    width: 58px;
    height: 72px;
  }
  .schedule {
    position: absolute;
    top: 420px;
    display: flex;
    align-items: center;
    gap: 12px;
    font-family: "Cinzel", serif;
    color: var(--ink);
  }
  .schedule--school { left: 68px; }
  .schedule--worship { left: 538px; }
  .schedule__label {
    font-weight: 600;
    font-size: 27px;
    line-height: 1.1;
    letter-spacing: 0.5px;
  }
  .schedule__time {
    font-weight: 600;
    font-size: 72px;
    line-height: 1;
  }
</style>
</head>
<body>
  <main class="sign" aria-label="Ferndale Chapel of Grace church sign">
    <svg class="sign-field" viewBox="0 0 1100 550" preserveAspectRatio="none" aria-hidden="true">
      <defs>
        <linearGradient id="gold-band" x1="0" y1="0" x2="1" y2="0">
          <stop offset="0" stop-color="var(--gold-bright)"/>
          <stop offset="0.28" stop-color="var(--gold-pale)"/>
          <stop offset="0.56" stop-color="var(--gold-deep)"/>
          <stop offset="0.8" stop-color="var(--gold-mid)"/>
          <stop offset="1" stop-color="var(--gold-pale)"/>
        </linearGradient>
      </defs>
      <rect width="1100" height="550" fill="url(#gold-band)"/>
      <path d="M0 0 H1100 V280 Q560 430 0 258 Z" fill="var(--night)"/>
      <path d="M0 258 Q560 430 1100 280" fill="none" stroke="var(--paper)" stroke-width="8"/>
    </svg>

    <div class="sign-name sign-name__place">Ferndale</div>
    <h1 class="sign-name sign-name__church">CHAPEL OF GRACE</h1>

    <svg class="cross" viewBox="0 0 58 72" aria-hidden="true">
      <defs>
        <linearGradient id="cross-gold" x1="0" y1="0" x2="0" y2="1">
          <stop offset="0" stop-color="var(--gold-title-top)"/>
          <stop offset="1" stop-color="var(--gold-title-bottom)"/>
        </linearGradient>
      </defs>
      <path d="M24 0 H34 V18 H58 V28 H34 V72 H24 V28 H0 V18 H24 Z" fill="url(#cross-gold)"/>
    </svg>

    <div class="schedule schedule--school">
      <div class="schedule__label">SUNDAY<br>SCHOOL</div>
      <div class="schedule__time">9:00AM</div>
    </div>
    <div class="schedule schedule--worship">
      <div class="schedule__label">WORSHIP<br>SERVICE</div>
      <div class="schedule__time">10:30AM</div>
    </div>
  </main>
</body>
</html>
```